need corporate, modern business card created for Consulting Company

I need a slick business card using elements from my website, as well as, integrating my pixelharbor-created logo (see files).

The business card needs to be:
1. Corporate and modern
2. Clean and professional

I've included a PSD with the logo/icon that you can use to create it. Feel free to try a metallic finish on the logo, make it bigger/small, underlay it. Whatever you need to do to make my card stand out.

Try a black background, or white background or gray.

The idea is for my card to be memorable as well as professional and corporate.

Target Market(s)

Corporate business in the US and Canada.

Industry/Entity Type

Business

Contact Information for Business Card

Clarity Through Smart Systems
Malcolm Tudd, Senior Partner
office: 1 877 555 0143
mobile: 1 519 555 0172
website: http://www.vextorial.com

Requirements
Must have
• Card-related information
• corporate, yet modern
• clean and professional
• incorporate the icon only
• must have an editable form when complete!
Nice to have
• metallic icon might be cool
• try it with white or black

```html
<!DOCTYPE html>
<html lang="en">
<head>
<meta charset="utf-8">
<title>Vextorial — Business Card</title>
<link rel="stylesheet" href="https://fonts.googleapis.com/css2?family=Fira+Sans:ital,wght@0,400;0,600;1,400&display=swap">
<style>
  :root {
    --backdrop: #ebebec;
    --card-dark-top: #8d8c90;
    --card-dark-bottom: #3a393c;
    --card-light: #f7f7f8;
    --brand-blue: #5470b4;
    --brand-blue-soft: #93a6d8;
    --tagline-grey: #8b8b8e;
    --ink: #2f2f33;
    --ink-muted: #55555a;
  }
  * { box-sizing: border-box; margin: 0; padding: 0; }
  html, body {
    width: 1200px; height: 720px; overflow: hidden;
    background: var(--backdrop);
    font-family: "Fira Sans", "Helvetica Neue", Arial, sans-serif;
  }
  .canvas {
    position: relative; width: 1200px; height: 720px;
  }
  .card {
    position: absolute; top: 210px;
    width: 525px; height: 300px;
    border-radius: 4px;
    box-shadow: 0 6px 18px rgba(0,0,0,0.18);
    overflow: hidden;
  }
  /* Front */
  .card--front {
    left: 50px;
    background: linear-gradient(160deg, var(--card-dark-top) 0%, var(--card-dark-bottom) 100%);
  }
  .brand {
    position: absolute; left: 70px; top: 98px;
    display: flex; align-items: center; gap: 18px;
  }
  .brand__mark {
    width: 54px; height: 54px;
    background: var(--brand-blue-soft);
    border-radius: 8px;
  }
  .brand__name {
    font-weight: 600; font-size: 66px; line-height: 1;
    letter-spacing: -1px;
    color: var(--brand-blue-soft);
  }
  .tagline {
    position: absolute; left: 0; right: 0; bottom: 48px;
    text-align: center;
    font-size: 15px; letter-spacing: 0.4px;
    color: var(--tagline-grey);
  }
  /* Back */
  .card--back {
    left: 625px;
    background: var(--card-light);
  }
  .card__accent {
    position: absolute; left: -40px; bottom: -40px;
    width: 170px; height: 170px;
    background: var(--brand-blue);
    border-radius: 22px;
  }
  .contact {
    position: absolute; left: 220px; top: 46px;
  }
  .contact__name {
    font-weight: 600; font-size: 34px; line-height: 1.05;
    color: var(--brand-blue);
  }
  .contact__role {
    font-style: italic; font-size: 13px;
    color: var(--ink-muted);
    margin-top: 2px;
  }
  .contact__list {
    list-style: none; margin-top: 26px;
  }
  .contact__item {
    display: flex; align-items: center; gap: 10px;
    font-size: 19px; line-height: 1; color: var(--ink);
    margin-bottom: 11px;
  }
  .contact__icon {
    width: 16px; height: 16px; flex: none;
    fill: none; stroke: var(--brand-blue); stroke-width: 1.6;
    stroke-linecap: round; stroke-linejoin: round;
  }
</style>
</head>
<body>
<main class="canvas">

  <section class="card card--front" aria-label="Card front">
    <div class="brand">
      <span class="brand__mark" aria-hidden="true"></span>
      <span class="brand__name">vextorial</span>
    </div>
    <p class="tagline">Clarity Through Smart Systems</p>
  </section>

  <section class="card card--back" aria-label="Card back">
    <span class="card__accent" aria-hidden="true"></span>
    <div class="contact">
      <h1 class="contact__name">Malcolm Tudd</h1>
      <p class="contact__role">Senior Partner</p>
      <ul class="contact__list">
        <li class="contact__item">
          <svg class="contact__icon" viewBox="0 0 16 16" aria-hidden="true">
            <circle cx="8" cy="8" r="7"/>
            <path d="M5.5 4.5l1.3 1.6-.8 1.1c.5 1 1.3 1.8 2.3 2.3l1.1-.8 1.6 1.3-.9 1.2c-2.6-.4-4.6-2.4-5-5z"/>
          </svg>
          1 877 555 0143
        </li>
        <li class="contact__item">
          <svg class="contact__icon" viewBox="0 0 16 16" aria-hidden="true">
            <rect x="4" y="1" width="8" height="14" rx="1.5"/>
            <path d="M7 12.5h2"/>
          </svg>
          1 519 555 0172
        </li>
        <li class="contact__item">
          <svg class="contact__icon" viewBox="0 0 16 16" aria-hidden="true">
            <rect x="1" y="3.5" width="14" height="9" rx="1"/>
            <path d="M1.5 4l6.5 5 6.5-5"/>
          </svg>
          provide email
        </li>
        <li class="contact__item">
          <svg class="contact__icon" viewBox="0 0 16 16" aria-hidden="true">
            <circle cx="8" cy="8" r="7"/>
            <path d="M1 8h14M8 1c2 2 2.8 4.3 2.8 7S10 13 8 15M8 1C6 3 5.2 5.3 5.2 8S6 13 8 15"/>
          </svg>
          www.vextorial.com
        </li>
      </ul>
    </div>
  </section>

</main>
</body>
</html>
```